Bag cardboard

Hi,

We are a language school, We want to provide our students with a bag cardboard each time they suscribe for a language course.

You can find in the attachement a pictutre of our current model.

For the new one, we want 3 logos to be included. (you can find in the attachement the 3 logos).

We also want our 3 adresses to be included in the model
Tunis - Imm Les Amandiers, 2ème étage 47 Rue du Lac Malawi, 1082 Les Rives du Parc 2
(phone logo) 71 482 613
(Email logo) tunis@parlomo.org

Sfax - Imm Yasmina, 4ème étage Rue Hedi Mbarki (en face de la poste), 3041 Sfax
(phone logo) 74 718 152
(email logo) sfax@parlomo.org

Sousse - 52 Ave Khalil Mardam (prés du rond point Belvédère au dessus du café Jasmin).
(phone logo) 73 594 206
(email logo) sousse@parlomo.org

The website needs to be cited also :
www.parlomo.org

And also the Linkwall Page
(Linkwall logo) /PARLOMO

Waiting for your suggestions !

Thx

```html
<!DOCTYPE html>
<html lang="fr">
<head>
<meta charset="utf-8">
<title>Parlomo Centre – sac carton</title>
<link rel="stylesheet" href="https://fonts.googleapis.com/css2?family=Oswald:wght@300;400;500&display=swap">
<style>
  :root {
    --backdrop: #d9d9d9;
    --panel-light: #87959a;
    --panel-dark: #5f6d6e;
    --fold-line: rgba(255,255,255,0.08);
    --band: #f4f4f4;
    --ink-light: #f2f2f2;
    --accent: #c9cb14;
    --ink-dark: #2b2b2b;
    --partner-teal: #1f8a7d;
    --partner-olive: #7a6a1e;
  }
  * { margin: 0; padding: 0; box-sizing: border-box; }
  html, body { width: 1200px; height: 1200px; overflow: hidden; }
  body {
    background: var(--backdrop);
    font-family: "Oswald", sans-serif;
    position: relative;
  }
  .bag-front {
    position: absolute;
    left: 200px; top: 100px;
    width: 800px; height: 1000px;
    background: radial-gradient(ellipse at 20% 45%, var(--panel-light) 0%, var(--panel-dark) 70%);
    overflow: hidden;
  }
  .gusset-fold {
    position: absolute; left: 0; right: 0; top: 760px; height: 175px;
    border-top: 2px solid var(--fold-line);
    background: linear-gradient(180deg, rgba(255,255,255,0.05), rgba(0,0,0,0.03));
  }
  .brand-mark {
    position: absolute; left: 60px; top: 420px;
    color: var(--ink-light);
    font-weight: 400;
    line-height: 0.9;
  }
  .brand-mark .brand-dot {
    position: absolute; left: -10px; top: -70px;
    width: 46px; height: 46px; border-radius: 50%;
    background: var(--accent);
  }
  .brand-mark .brand-name { font-size: 130px; letter-spacing: -2px; display: block; }
  .brand-mark .brand-sub { font-size: 70px; display: block; padding-left: 175px; }
  .online-links {
    position: absolute; left: 470px; top: 530px;
    color: var(--ink-light);
    font-weight: 400;
    letter-spacing: 3px;
    font-size: 22px;
  }
  .online-links .website {
    display: block; padding: 0 0 6px 14px;
    border-bottom: 1px solid var(--ink-light);
  }
  .online-links .social {
    display: block; margin-top: 8px; padding-left: 8px;
  }
  .online-links .social-label {
    background: var(--ink-light); color: var(--panel-dark);
    padding: 0 4px; margin-right: 4px;
  }
  .address-band {
    position: absolute; left: 0; right: 0; bottom: 0; height: 165px;
    background: var(--band);
    display: flex; align-items: flex-start;
    padding: 25px 20px 0 14px;
    gap: 26px;
  }
  .office {
    width: 150px;
    color: var(--ink-dark);
    font-size: 10px; font-weight: 400;
    line-height: 1.35;
    text-transform: uppercase;
  }
  .office.sousse { width: 165px; }
  .partners {
    margin-left: auto; margin-top: 45px;
    display: flex; gap: 34px; align-items: center;
  }
  .partner {
    display: flex; align-items: center; gap: 6px;
    font-size: 18px; font-weight: 400;
  }
  .partner .partner-shape { width: 16px; height: 16px; }
  .partner.verdalo { color: var(--partner-teal); }
  .partner.verdalo .partner-shape { background: var(--partner-teal); }
  .partner.ristano { color: var(--partner-olive); }
  .partner.ristano .partner-shape { background: var(--partner-olive); border-radius: 50%; }
</style>
</head>
<body>
  <main class="bag-front">
    <div class="gusset-fold"></div>

    <div class="brand-mark">
      <span class="brand-dot"></span>
      <span class="brand-name">parlomo</span>
      <span class="brand-sub">centre</span>
    </div>

    <div class="online-links">
      <span class="website">WWW.PARLOMO.ORG</span>
      <span class="social"><span class="social-label">LINKWALL</span>/PARLOMO</span>
    </div>

    <section class="address-band">
      <p class="office tunis">Tunis - Imm Les Amandiers,<br>2ème étage 47 Rue du Lac Malawi,<br>1082 Les Rives du Parc 2<br>71 482 613<br>tunis@parlomo.org</p>
      <p class="office sfax">Sfax - Imm Yasmina,<br>4ème étage Rue Hedi Mbarki<br>(en face de la poste), 3041 Sfax<br>74 718 152<br>sfax@parlomo.org</p>
      <p class="office sousse">Sousse - 52 Ave Khalil Mardam<br>(prés du rond point Belvédère<br>au dessus du café Jasmin)<br>73 594 206<br>sousse@parlomo.org</p>
      <div class="partners">
        <span class="partner verdalo"><span class="partner-shape"></span>VERDALO</span>
        <span class="partner ristano"><span class="partner-shape"></span>ristano</span>
      </div>
    </section>
  </main>
</body>
</html>
```